Design of business signage for outside store front

We need signage designed for outside a store front.  We already have a logo, colours and font that we would like to use but would like some ideas as regards layout/design of the signage.  The final product will be for the use of the installer to produce and install the signage.  Attached are files with our logo and font and a picture of the current signage which needs to be replaced.  The size and shape of the signage will be the same as the current signage, its just the design/layout that we would like changed.
N.B. We would like two versions if possible, one with the web address and one without the web address to see what they look like.

```html
<!DOCTYPE html>
<html lang="en">
<head>
<meta charset="utf-8">
<title>Marlow Pantry – Storefront Sign</title>
<link rel="stylesheet" href="https://fonts.googleapis.com/css2?family=Marcellus&family=Raleway:wght@500&display=swap">
<style>
  :root {
    --maroon: #8c2432;
    --gold: #f3d034;
    --gold-line: #e0a92a;
    --gold-soft: #f6e59a;
    --white: #ffffff;
    --page: #ffffff;
  }
  html, body {
    margin: 0;
    padding: 0;
    width: 922px;
    height: 1200px;
    overflow: hidden;
    background: var(--page);
  }
  .sign {
    position: absolute;
    left: 31px;
    top: 384px;
    width: 860px;
    height: 432px;
    display: block;
  }
  .sign__board { fill: var(--maroon); }
  .sign__frame { fill: none; stroke: var(--gold-line); stroke-width: 1.2; }
  .sign__name {
    font-family: "Marcellus", serif;
    fill: var(--white);
  }
  .sign__name--top { font-size: 104px; }
  .sign__name--bottom { font-size: 74px; }
  .sign__tagline {
    font-family: "Raleway", sans-serif;
    font-weight: 500;
    font-size: 27px;
    fill: var(--white);
  }
  .sign__web-bar { fill: var(--gold); }
  .sign__web {
    font-family: "Raleway", sans-serif;
    font-weight: 500;
    font-size: 25px;
    fill: var(--maroon);
  }
</style>
</head>
<body>
  <svg class="sign" viewBox="0 0 860 432" xmlns="http://www.w3.org/2000/svg" aria-label="Marlow Pantry storefront sign">
    <defs>
      <linearGradient id="emblem-fill" x1="0" y1="0" x2="0" y2="1">
        <stop offset="0" stop-color="#ffffff"/>
        <stop offset="0.55" stop-color="#fbf3d2"/>
        <stop offset="1" stop-color="#f6e59a"/>
      </linearGradient>
    </defs>

    <rect class="sign__board" x="0" y="0" width="860" height="432"/>
    <rect class="sign__frame" x="18" y="18" width="824" height="396"/>

    <rect class="sign__emblem" x="58" y="55" width="187" height="326" fill="url(#emblem-fill)"
          role="img" aria-label="Brand emblem: dancing figure wrapped in a flowing gold ribbon"/>

    <text class="sign__name sign__name--top" x="300" y="140" textLength="500" lengthAdjust="spacingAndGlyphs">MARLOW</text>
    <text class="sign__name sign__name--bottom" x="300" y="216" textLength="500" lengthAdjust="spacingAndGlyphs">PANTRY</text>
    <text class="sign__tagline" x="300" y="274" textLength="504" lengthAdjust="spacing">Spanish Artisan Foods</text>

    <rect class="sign__web-bar" x="302" y="331" width="540" height="43"/>
    <text class="sign__web" x="532" y="361" textLength="268" lengthAdjust="spacing">www.marlowpantry.com</text>
  </svg>
</body>
</html>
```